Website design for labour force (commercial truck driver) company

Looking for a Wordpress template (or design files in conjunction with a free Wordpress template).
Company tag line:
Tenvora – On Demand, Professional Drivers
Real Drivers | Real Standards | Real Results
Logo design has already been completed and is attached

Company provides contract drivers to trucking companies. Target market is both the trucking companies looking for drivers and drivers looking for work.
Design to encompass header / footer and basic page design, navigation menu, home page, contact page. Customer will add content and additional pages over time.

```html
<!DOCTYPE html>
<html lang="en">
<head>
<meta charset="utf-8">
<title>Tenvora – On Demand, Professional Drivers</title>
<link href="https://fonts.googleapis.com/css2?family=Archivo+Black&family=Montserrat:ital,wght@0,400;0,500;0,600;0,700;1,400&display=swap" rel="stylesheet">
<style>
:root{
  --green:#128560;
  --green-dark:#0d6b4c;
  --ink:#151515;
  --muted:#6f6f6f;
  --field:#f1f1f1;
  --white:#ffffff;
  --night:#1c1d1d;
  --star:#f2a51e;
}
*{margin:0;padding:0;box-sizing:border-box}
html,body{width:1200px;height:4185px;overflow:hidden}
body{position:relative;background:var(--white);font-family:"Montserrat",sans-serif;color:var(--ink)}
.abs{position:absolute}
.display{font-family:"Archivo Black",sans-serif;text-transform:uppercase;letter-spacing:-0.5px;line-height:1}
.btn{position:absolute;display:flex;align-items:center;justify-content:center;border-radius:26px;font-weight:600;font-size:15px;color:var(--white);background:var(--green)}
.btn.ghost{background:transparent;border:2px solid var(--white)}
.center{text-align:center}

/* header */
.brand{position:absolute;display:flex;align-items:center;gap:12px;font-family:"Archivo Black",sans-serif;font-size:30px;color:var(--white)}
.brand-dot{width:34px;height:34px;border-radius:50%;background:var(--green)}
.nav-link{position:absolute;top:38px;font-size:14px;line-height:22px;color:var(--white);white-space:nowrap}
.nav-sep{position:absolute;top:38px;width:1.5px;height:22px;background:rgba(255,255,255,.8)}
.contact-pill{position:absolute;left:939px;top:24px;width:172px;height:52px;border-radius:26px;background:var(--white);display:flex;align-items:center;gap:14px;padding-left:6px;font-size:14px;font-weight:500;white-space:nowrap}
.contact-pill i{width:42px;height:42px;border-radius:50%;background:var(--green);display:flex;align-items:center;justify-content:center;flex:none}

/* hero */
.hero{position:absolute;left:0;top:0;width:1200px;height:726px;background:
  radial-gradient(ellipse 420px 520px at 880px 330px,#8a8f94 0%,#4d5156 45%,transparent 75%),
  linear-gradient(90deg,#0d0f10 0%,#1e2125 40%,#3b3f44 70%,#6d7278 100%)}
.hero-line1{left:89px;top:250px;font-size:58px;color:var(--white)}
.hero-line2{left:89px;top:318px;font-size:78px;color:transparent;-webkit-text-stroke:2px var(--green)}
.hero-line3{left:89px;top:404px;font-size:33px;color:var(--white)}
.hero-tag{left:89px;top:452px;font-size:14px;color:var(--white)}

/* feature icons */
.badge{position:absolute;width:114px;height:114px;border-radius:50%;background:var(--white);box-shadow:0 4px 12px rgba(0,0,0,.15);display:flex;align-items:center;justify-content:center}
.badge>div{width:100px;height:100px;border-radius:50%;background:var(--green);display:flex;align-items:center;justify-content:center}
.badge-label{position:absolute;width:240px;font-family:"Archivo Black",sans-serif;font-size:16px;text-transform:uppercase;text-align:center}
.badge-sub{position:absolute;width:260px;font-size:14px;color:var(--muted);text-align:center}

/* about */
.photo{position:absolute;border-radius:22px}
.h2{font-size:42px}
.body-copy{font-size:14.5px;line-height:22px;color:var(--muted)}

/* why */
.landscape{position:absolute;left:0;top:1610px;width:1200px;height:440px;background:linear-gradient(180deg,#ffffff 0%,#d9cfc4 22%,#8d7764 48%,#5a4636 72%,#3e3024 100%)}
.arrow{position:absolute;width:46px;height:46px;border-radius:50%;display:flex;align-items:center;justify-content:center;box-shadow:0 2px 8px rgba(0,0,0,.2)}
.card-title{position:absolute;width:290px;text-align:center;font-family:"Archivo Black",sans-serif;font-size:17px}
.card-desc{position:absolute;width:270px;text-align:center;font-size:14px;line-height:21px;color:var(--muted)}

/* testimonials */
.t-card{position:absolute;background:var(--white);border-radius:22px;box-shadow:0 4px 20px rgba(0,0,0,.1)}
.quote-mark{position:absolute;font-family:"Archivo Black",sans-serif;font-size:72px;color:#b5dcc8;line-height:1}
.avatar{position:absolute;width:72px;height:72px;border-radius:50%;background:linear-gradient(160deg,#7aa8d6,#3d5a78)}
.field{position:absolute;background:var(--field);border-radius:14px;font-size:13px;color:#7a7a7a;padding:18px 18px}

/* footer */
.footer{position:absolute;left:0;top:3573px;width:1200px;height:612px;background:
  linear-gradient(180deg,#262828 0%,#1d1e1e 45%,#2a2622 80%,#1a1a1a 100%)}
.foot-h{position:absolute;font-family:"Archivo Black",sans-serif;font-size:25px;color:var(--white);text-transform:uppercase}
.foot-link{position:absolute;font-size:14px;color:var(--white)}
.rule{position:absolute;left:89px;width:1022px;height:1px;background:rgba(255,255,255,.35)}
.social{position:absolute;width:38px;height:38px;border-radius:50%}
</style>
</head>
<body>

<!-- HERO -->
<div class="hero" role="img" aria-label="Truck driver with crossed arms standing in front of a white semi truck"></div>
<div class="brand" style="left:89px;top:28px"><span class="brand-dot"></span>Tenvora</div>
<nav>
  <span class="nav-link" style="left:474px">Home</span>
  <span class="nav-sep" style="left:535px"></span>
  <span class="nav-link" style="left:555px">Hire a Driver</span>
  <span class="nav-sep" style="left:660px"></span>
  <span class="nav-link" style="left:681px">Find Driving Jobs</span>
  <span class="nav-sep" style="left:822px"></span>
  <span class="nav-link" style="left:842px">About Us</span>
</nav>
<div class="contact-pill"><i><svg width="20" height="20" viewBox="0 0 24 24" fill="none" stroke="#fff" stroke-width="2"><path d="M5 3h4l2 5-3 2a12 12 0 0 0 6 6l2-3 5 2v4a2 2 0 0 1-2 2A17 17 0 0 1 3 5a2 2 0 0 1 2-2z"/></svg></i>Contact Us</div>

<div class="abs display hero-line1">Tenvora –</div>
<div class="abs display hero-line2">On Demand,</div>
<div class="abs display hero-line3">Professional Drivers</div>
<div class="abs hero-tag">Reliable. Experienced. Ready to Roll.</div>
<div class="btn" style="left:89px;top:494px;width:163px;height:46px">Hire a Driver</div>
<div class="btn ghost" style="left:260px;top:494px;width:203px;height:46px">Find Driving Jobs</div>

<!-- VALUES -->
<div class="badge" style="left:292px;top:783px"><div>
  <svg width="54" height="54" viewBox="0 0 54 54" fill="none" stroke="#fff" stroke-width="3"><circle cx="27" cy="27" r="20"/><circle cx="27" cy="27" r="5"/><path d="M7 27h15M32 27h15M27 32v15"/></svg></div></div>
<div class="badge" style="left:544px;top:783px"><div>
  <svg width="54" height="54" viewBox="0 0 54 54" fill="none" stroke="#fff" stroke-width="3"><rect x="11" y="9" width="28" height="36" rx="3"/><path d="M19 9v-3h12v3M17 20h16M17 28h10"/><circle cx="38" cy="38" r="8"/><path d="M34 38l3 3 5-5"/></svg></div></div>
<div class="badge" style="left:792px;top:783px"><div>
  <svg width="54" height="54" viewBox="0 0 54 54" fill="none" stroke="#fff" stroke-width="3"><rect x="11" y="9" width="28" height="36" rx="3"/><path d="M19 9v-3h12v3M19 34V26M25 34V20M31 34V28"/><circle cx="38" cy="38" r="8"/><path d="M34 38l3 3 5-5"/></svg></div></div>
<div class="badge-label" style="left:229px;top:914px">Real Drivers</div>
<div class="badge-label" style="left:481px;top:914px">Real Standards</div>
<div class="badge-label" style="left:729px;top:914px">Real Results</div>

<!-- ABOUT -->
<div class="photo" role="img" aria-label="Smiling truck driver in a plaid shirt standing beside parked trucks" style="left:140px;top:1028px;width:385px;height:401px;background:linear-gradient(160deg,#cfdbe6 0%,#9fb0bf 45%,#5a6470 100%)"></div>
<div class="abs display h2" style="left:577px;top:1064px;line-height:48px">About Tenvora<br>Limited</div>
<p class="abs body-copy" style="left:577px;top:1168px;width:480px">At Tenvora, we connect trucking companies with qualified, contract drivers — fast. Whether you're looking to fill a last-minute shift or build a long-term partnership, our experienced drivers are ready to hit the road.</p>
<p class="abs body-copy" style="left:577px;top:1272px;width:480px">We believe in high standards, safety, and results that move your business forward.</p>
<div class="btn" style="left:577px;top:1338px;width:147px;height:46px">Read More</div>

<!-- DRIVER CTA + WHY -->
<div class="landscape" role="img" aria-label="Desert highway landscape with distant mountains at dusk"></div>
<div class="abs display h2 center" style="left:0;top:1533px;width:1200px">Are You A Driver?</div>
<p class="abs body-copy center" style="left:280px;top:1589px;width:640px">Join the Tenvora network and start getting real driving jobs. We connect professional CDL drivers with top-paying opportunities.</p>
<div class="btn" style="left:526px;top:1653px;width:148px;height:46px">Apply Now</div>

<div class="abs display center" style="left:0;top:1804px;width:1200px;font-size:38px;color:var(--white)">Why Choose</div>
<div class="abs display center" style="left:0;top:1848px;width:1200px;font-size:58px;color:var(--white)">Tenvora?</div>

<div class="photo" role="img" aria-label="Business handshake over a signed contract" style="left:179px;top:1934px;width:269px;height:263px;background:linear-gradient(150deg,#3d4a5c,#8a95a3 60%,#e8e6e2)"></div>
<div class="photo" role="img" aria-label="Smiling driver seated at the wheel inside a truck cab" style="left:464px;top:1934px;width:270px;height:263px;background:linear-gradient(150deg,#c9ced3,#7f8790 55%,#3a3f45)"></div>
<div class="photo" role="img" aria-label="Driver giving a thumbs up from the open door of a blue truck" style="left:752px;top:1934px;width:269px;height:263px;background:linear-gradient(150deg,#2f5f9c,#6b86a8 50%,#d8c7b0)"></div>
<div class="arrow" style="left:87px;top:2025px;background:var(--white)"><svg width="12" height="12" viewBox="0 0 12 12" fill="none" stroke="#151515" stroke-width="2"><path d="M8 2L4 6l4 4"/></svg></div>
<div class="arrow" style="left:1065px;top:2025px;background:var(--green)"><svg width="12" height="12" viewBox="0 0 12 12" fill="none" stroke="#fff" stroke-width="2"><path d="M4 2l4 4-4 4"/></svg></div>
<div class="card-title" style="left:168px;top:2214px">FLEXIBLE CONTRACTS</div>
<div class="card-title" style="left:454px;top:2214px">NATIONWIDE NETWORK</div>
<div class="card-title" style="left:742px;top:2214px">DRIVER SUPPORT</div>
<div class="card-desc" style="left:173px;top:2239px">On-demand or long-term we adapt to your needs.</div>
<div class="card-desc" style="left:466px;top:2239px">Wherever you are, we've got drivers near you.</div>
<div class="card-desc" style="left:752px;top:2239px">We support our drivers with 24/7 help, training, and guidance.</div>

<!-- HOW IT WORKS -->
<div class="abs display h2 center" style="left:0;top:2368px;width:1200px">How It Works</div>
<div class="badge" style="left:245px;top:2436px"><div>
  <svg width="54" height="54" viewBox="0 0 54 54" fill="none" stroke="#fff" stroke-width="3"><circle cx="27" cy="27" r="20"/><circle cx="27" cy="27" r="5"/><path d="M7 27h15M32 27h15M27 32v15"/></svg></div></div>
<div class="badge" style="left:544px;top:2436px"><div>
  <svg width="54" height="54" viewBox="0 0 54 54" fill="none" stroke="#fff" stroke-width="3"><rect x="11" y="9" width="28" height="36" rx="3"/><path d="M19 9v-3h12v3M17 20h16M17 28h10"/><circle cx="38" cy="38" r="8"/><path d="M34 38l3 3 5-5"/></svg></div></div>
<div class="badge" style="left:838px;top:2436px"><div>
  <svg width="54" height="54" viewBox="0 0 54 54" fill="none" stroke="#fff" stroke-width="3"><rect x="11" y="9" width="28" height="36" rx="3"/><path d="M19 9v-3h12v3M19 34V26M25 34V20M31 34V28"/><circle cx="38" cy="38" r="8"/><path d="M34 38l3 3 5-5"/></svg></div></div>
<div class="badge-label" style="left:182px;top:2570px">Request A Driver</div>
<div class="badge-label" style="left:461px;top:2570px;width:280px">Drive With Confidence</div>
<div class="badge-label" style="left:775px;top:2570px">Get Matched Fast</div>
<div class="badge-sub" style="left:172px;top:2592px">Submit your job details.</div>
<div class="badge-sub" style="left:461px;top:2592px;width:264px">Reliable, professional service.</div>
<div class="badge-sub" style="left:765px;top:2592px">We assign a qualified.</div>

<!-- TESTIMONIALS -->
<div class="abs display h2 center" style="left:0;top:2699px;width:1200px">Testimonials</div>
<div class="t-card" style="left:222px;top:2770px;width:100px;height:215px"></div>
<div class="quote-mark" style="left:243px;top:2808px">“</div>
<div class="abs display" style="left:222px;top:2867px;width:100px;text-align:center;font-size:13px">Devon K.</div>
<div class="avatar" role="img" aria-label="Client portrait" style="left:236px;top:2897px"></div>

<div class="t-card" style="left:333px;top:2770px;width:533px;height:215px"></div>
<div class="abs" style="left:358px;top:2799px;display:flex;gap:3px">
  <svg width="105" height="20" viewBox="0 0 105 20" fill="var(--star)"><g id="s"><path d="M10 1l2.6 5.8 6.3.6-4.8 4.2 1.4 6.2L10 14.6 4.5 17.8l1.4-6.2L1.1 7.4l6.3-.6z"/></g><use href="#s" x="21"/><use href="#s" x="42"/><use href="#s" x="63"/><use href="#s" x="84"/></svg>
</div>
<p class="abs" style="left:358px;top:2834px;width:490px;font-size:18px;line-height:27px;font-style:italic;color:var(--muted)">"Tenvora helped us stay on schedule during a busy season The driver showed up on time was well trained and professional."</p>
<div class="abs display" style="left:356px;top:2931px;font-size:16px">Reed M., Fleet Manager</div>

<div class="t-card" style="left:879px;top:2770px;width:97px;height:215px"></div>
<div class="quote-mark" style="left:899px;top:2808px">“</div>
<div class="abs display" style="left:879px;top:2867px;width:97px;text-align:center;font-size:13px">Devon K.</div>
<div class="avatar" role="img" aria-label="Client portrait" style="left:892px;top:2897px"></div>

<!-- FORM -->
<div class="abs display h2 center" style="left:0;top:3079px;width:1200px">Testimonials</div>
<div class="field" style="left:255px;top:3151px;width:336px;height:53px">Name*</div>
<div class="field" style="left:607px;top:3151px;width:338px;height:53px">Email*</div>
<div class="field" style="left:255px;top:3216px;width:336px;height:53px">Phone*</div>
<div class="field" style="left:607px;top:3216px;width:338px;height:53px">Address*</div>
<div class="field" style="left:255px;top:3280px;width:690px;height:112px;padding-top:14px">Message*</div>
<div class="btn" style="left:520px;top:3423px;width:160px;height:47px">Submit Now</div>

<!-- FOOTER -->
<div class="footer" role="img" aria-label="Dark open road stretching toward the horizon"></div>
<div class="abs display" style="left:89px;top:3630px;font-size:42px;line-height:49px;color:var(--white)">Ready To Drive<br>Your Business Forward?</div>
<div class="abs" style="left:89px;top:3734px;font-size:14px;color:var(--white)">Let Tenvora provide the talent you need.</div>
<div class="btn" style="left:773px;top:3673px;width:161px;height:47px">Hire a Driver</div>
<div class="btn ghost" style="left:942px;top:3673px;width:169px;height:47px">Apply to Drive</div>
<div class="rule" style="top:3800px"></div>

<div class="brand" style="left:89px;top:3934px;font-size:27px"><span class="brand-dot" style="width:30px;height:30px"></span>Tenvora</div>

<div class="foot-h" style="left:352px;top:3868px">Quick Link</div>
<div class="foot-link" style="left:352px;top:3911px">Home</div>
<div class="foot-link" style="left:352px;top:3937px">Hire a Driver</div>
<div class="foot-link" style="left:352px;top:3963px">Find Driving Jobs</div>
<div class="foot-link" style="left:352px;top:3990px">About Us</div>
<div class="foot-link" style="left:352px;top:4017px">Contact Us</div>

<div class="foot-h" style="left:628px;top:3868px">Contact Us</div>
<svg class="abs" style="left:628px;top:3913px" width="12" height="12" viewBox="0 0 24 24" fill="var(--green)"><path d="M5 2h4l2 6-3 2a12 12 0 0 0 6 6l2-3 6 2v4a2 2 0 0 1-2 2A19 19 0 0 1 3 4a2 2 0 0 1 2-2z"/></svg>
<div class="foot-link" style="left:648px;top:3910px;font-size:13px;line-height:17px">Phone<br>(800) 555-0148</div>
<svg class="abs" style="left:627px;top:3961px" width="14" height="11" viewBox="0 0 14 11"><rect width="14" height="11" rx="1.5" fill="var(--green)"/><path d="M1 1.5l6 4.5 6-4.5" fill="none" stroke="#1d1e1e" stroke-width="1.3"/></svg>
<div class="foot-link" style="left:648px;top:3958px;font-size:13px;line-height:17px">Email<br>info@tenvora.com</div>
<svg class="abs" style="left:628px;top:4012px" width="12" height="16" viewBox="0 0 12 16" fill="var(--green)"><path d="M6 0a6 6 0 0 1 6 6c0 4.5-6 10-6 10S0 10.5 0 6a6 6 0 0 1 6-6zm0 3.5A2.5 2.5 0 1 0 6 8.5 2.5 2.5 0 0 0 6 3.5z"/></svg>
<div class="foot-link" style="left:648px;top:4007px;font-size:13px;line-height:17px">Address<br>48 Haulway Road, Dallas, TX 75207</div>

<div class="foot-h" style="left:939px;top:3868px">Follow Us</div>
<div class="social" style="left:939px;top:3914px;background:#3a5a9a"></div>
<div class="social" style="left:983px;top:3914px;background:#1d9bd8"></div>
<div class="social" style="left:1027px;top:3914px;background:#1a5a8a"></div>
<div class="social" style="left:1071px;top:3914px;background:#c9407a"></div>

<div class="rule" style="top:4109px"></div>
<div class="abs center" style="left:0;top:4138px;width:1200px;font-size:14px;color:var(--white)">© 2025 Tenvora Limited. All rights reserved.</div>
<div class="arrow" style="left:1126px;top:4082px;width:54px;height:54px;background:var(--green)"><svg width="14" height="14" viewBox="0 0 14 14" fill="none" stroke="#fff" stroke-width="2"><path d="M3 9l4-4 4 4"/></svg></div>

</body>
</html>
```